Website Design for Landscaping/Concrete Company

I need a website that is informative about what my company does and also offers before and after pictures of completed work. I already have a logo. The website must say "FREE ESTIMATES" somewhere and list a phone number. I would like to stick with the logo colors or similar (black and lime green).
Services Offered by Dornel Contractors:
Landscaping
Mowing
Concrete
Sidewalks
Brush Removal
Land Beautification

Please list the company name in large letters DORNEL CONTRACTORS
and also the contact information in large font.

Right now I am looking for a somewhat coverpage for my website. I don't have a lot of information for people to point and click on yet. Id like to get a coverpage to get my name out and then have a designer come back in a few months and update with more pictures and information.
Updates

If allowed please submit projects after due date. I made a mistake and only posted for one day. Thanks.

Coding

Coded - Design and coding required

```html
<!DOCTYPE html>
<html lang="en">
<head>
<meta charset="utf-8">
<title>Dornel Contractors</title>
<link rel="stylesheet" href="https://fonts.googleapis.com/css2?family=Audiowide&family=Open+Sans:wght@400;600;700&display=swap">
<style>
:root{
  --black:#000;
  --ink:#0b0b0b;
  --lime:#8dc63f;
  --lime-bright:#a6d83c;
  --leaf:#4d7a17;
  --forest:#2c4a0c;
  --white:#fff;
  --muted:#bdbdbd;
  --display:"Audiowide", sans-serif;
  --body:"Open Sans", sans-serif;
}
*{margin:0;padding:0;box-sizing:border-box}
html,body{width:1200px;height:3612px;overflow:hidden;background:var(--black);font-family:var(--body);color:var(--white)}
.page{position:relative;width:1200px;height:3612px}
.abs{position:absolute}

/* header */
.brand{left:140px;top:0;width:190px;height:150px;background:var(--black);border-radius:0 0 95px 95px;display:flex;flex-direction:column;align-items:center;justify-content:center;z-index:3;gap:8px}
.brand-square{width:34px;height:34px;background:var(--lime)}
.brand-name{font-family:var(--display);font-size:20px;color:var(--lime);text-align:center;line-height:1.1}
.topbar{left:0;top:0;width:1200px;height:84px;background:rgba(0,0,0,.82);z-index:2}
.call{right:250px;top:28px;font-size:20px;font-weight:600;display:flex;align-items:center;gap:10px;z-index:3}
.btn{display:inline-block;background:var(--lime);color:var(--black);font-weight:700;font-size:16px;padding:8px 18px;text-transform:uppercase;letter-spacing:.5px}
.top-btn{right:80px;top:24px;z-index:3;color:var(--white);background:var(--leaf);border:2px solid var(--lime)}
.nav{left:560px;top:88px;width:640px;height:44px;background:var(--lime);clip-path:polygon(24px 0,100% 0,100% 100%,0 100%);display:flex;align-items:center;gap:46px;padding-left:60px;z-index:3}
.nav a{color:var(--black);font-weight:700;font-size:16px;text-decoration:none}
.nav a.active{color:var(--white)}

/* hero */
.hero{left:0;top:0;width:1200px;height:790px;background:linear-gradient(180deg,#3e6fb6 0%,#7fa7d8 35%,#9aa3a8 55%,#4b5257 70%,#3d6a22 80%,#2b4a15 100%)}
.hero-shade{left:0;top:0;width:1200px;height:790px;background:linear-gradient(90deg,rgba(0,0,0,.55),rgba(0,0,0,0) 60%)}
.hero-title{left:140px;top:318px;font-family:var(--display);font-size:72px;line-height:1.05;letter-spacing:4px}
.hero-sub{left:142px;top:492px;font-size:22px;font-weight:600}
.hero-btn{left:142px;top:556px;font-size:16px}
.dots{right:64px;top:428px;display:flex;flex-direction:column;gap:12px}
.dots span{width:10px;height:10px;border-radius:50%;background:var(--white)}

/* dividers */
.divider{left:0;width:1200px;height:60px}

/* about */
.about-mark{left:170px;top:880px;width:320px;height:300px;display:flex;flex-direction:column;align-items:flex-start;justify-content:center;gap:18px}
.about-mark .brand-square{width:90px;height:90px}
.about-mark .brand-name{font-size:40px;text-align:left}
.about-h{left:570px;top:850px;font-family:var(--display);font-size:50px;letter-spacing:3px}
.about-h2{left:570px;top:920px;font-family:var(--display);font-size:30px;color:var(--lime);letter-spacing:2px}
.about-p{left:570px;top:980px;width:500px;font-size:14px;line-height:1.65;color:var(--muted)}
.about-btn{left:570px;top:1206px}

/* section titles */
.title{left:0;width:1200px;text-align:center;font-family:var(--display);font-size:48px;letter-spacing:4px}
.title em{font-style:normal;color:var(--lime)}

/* services */
.service{width:300px;font-size:14px;color:var(--muted);line-height:1.45}
.service h3{font-size:20px;color:var(--white);font-weight:700;margin-bottom:6px}
.service.left{text-align:right}
.core{left:520px;top:1752px;width:160px;height:160px;border-radius:50%;display:flex;align-items:center;justify-content:center;flex-direction:column;gap:6px}
.core .brand-name{font-size:17px}

/* gallery */
.photo{position:absolute}

/* contact */
.contact-band{left:0;top:2980px;width:1200px;height:632px;background:linear-gradient(180deg,var(--forest) 0%,#1c3206 60%,#0d1a02 100%)}
.col-h{font-size:26px;font-weight:700}
.field{position:absolute;background:var(--white);color:#888;font-size:13px;padding:8px 10px;height:34px}
.info{font-size:16px;display:flex;align-items:flex-start;gap:14px;line-height:1.4}
.pin{width:26px;height:26px;border-radius:50%;background:var(--white);flex:none;display:flex;align-items:center;justify-content:center}
.social{display:flex;gap:12px}
.social span{width:28px;height:28px;border-radius:50%;background:var(--white)}
.footer{left:0;top:3560px;width:1200px;height:52px;background:var(--black);display:flex;align-items:center;justify-content:center;font-size:13px;color:var(--muted)}
</style>
</head>
<body>
<div class="page">

  <!-- hero -->
  <div class="abs hero" role="img" aria-label="Photo of a modern commercial building with a lawn under a blue sky"></div>
  <div class="abs hero-shade"></div>
  <div class="abs topbar"></div>
  <div class="abs brand"><span class="brand-square"></span><span class="brand-name">DORNEL<br>CONTRACTORS</span></div>
  <div class="abs call">
    <svg width="26" height="26" viewBox="0 0 24 24"><circle cx="12" cy="12" r="11" fill="none" stroke="#8dc63f" stroke-width="2"/><path d="M8 6l2 3-1.5 1.5a8 8 0 0 0 5 5L15 14l3 2-1 2.5C11 18 6 13 5.5 7z" fill="#8dc63f"/></svg>
    Call Us : 1 888 888 8888
  </div>
  <div class="abs btn top-btn">Free Estimates</div>
  <nav class="abs nav">
    <a class="active">Home</a><a>About</a><a>Services</a><a>Gallery</a><a>Contact</a>
    <svg width="18" height="18" viewBox="0 0 20 20"><circle cx="8" cy="8" r="6" fill="none" stroke="#000" stroke-width="2.5"/><path d="M12.5 12.5l5 5" stroke="#000" stroke-width="2.5"/></svg>
  </nav>
  <h1 class="abs hero-title">DORNEL<br>CONTRACTORS</h1>
  <p class="abs hero-sub">Lorem ipsum dolor sit amet consectetur adipiscing elit</p>
  <div class="abs btn hero-btn">Free Estimates</div>
  <div class="abs dots"><span></span><span></span><span></span></div>
  <svg class="abs divider" style="top:740px" viewBox="0 0 1200 60" preserveAspectRatio="none">
    <polygon points="0,60 0,40 600,8 1200,40 1200,60" fill="#000"/>
    <polyline points="0,40 600,8 1200,40" fill="none" stroke="#fff" stroke-width="3"/>
  </svg>

  <!-- about -->
  <div class="abs about-mark"><span class="brand-square"></span><span class="brand-name">DORNEL<br>CONTRACTORS</span></div>
  <h2 class="abs about-h">ABOUT</h2>
  <h3 class="abs about-h2">DORNEL CONTRACTORS</h3>
  <p class="abs about-p">Lorem ipsum dolor sit amet consectetur adipiscing elit sed do eiusmod tempor incididunt ut labore et dolore magna aliqua. Ut enim ad minim veniam quis nostrud exercitation ullamco laboris nisi ut aliquip ex ea commodo consequat. Duis aute irure dolor in reprehenderit in voluptate velit esse cillum dolore eu fugiat nulla pariatur. Excepteur sint occaecat cupidatat non proident sunt in culpa qui officia deserunt mollit anim id est laborum. Sed ut perspiciatis unde omnis iste natus error sit voluptatem accusantium doloremque laudantium totam rem aperiam.</p>
  <div class="abs btn about-btn">Get Started</div>
  <svg class="abs divider" style="top:1300px" viewBox="0 0 1200 60" preserveAspectRatio="none">
    <polyline points="0,10 600,44 1200,10" fill="none" stroke="#8dc63f" stroke-width="3"/>
  </svg>

  <!-- services -->
  <h2 class="abs title" style="top:1482px">OUR <em>SERVICES</em></h2>
  <svg class="abs" style="left:0;top:1580px" width="1200" height="480" viewBox="0 1580 1200 480">
    <circle cx="600" cy="1832" r="140" fill="#050505" stroke="#1c1c1c" stroke-width="20"/>
    <circle cx="600" cy="1832" r="150" fill="none" stroke="#8dc63f" stroke-width="2"/>
    <g stroke="#8dc63f" stroke-width="2" fill="none">
      <path d="M470 1660 L504 1660 L530 1722"/>
      <path d="M470 1808 L450 1808"/>
      <path d="M470 1970 L504 1970 L530 1944"/>
      <path d="M730 1660 L696 1660 L670 1722"/>
      <path d="M730 1808 L750 1808"/>
      <path d="M730 1970 L696 1970 L670 1944"/>
    </g>
    <g fill="#8dc63f">
      <circle cx="532" cy="1724" r="6"/><circle cx="452" cy="1808" r="6"/><circle cx="532" cy="1942" r="6"/>
      <circle cx="668" cy="1724" r="6"/><circle cx="748" cy="1808" r="6"/><circle cx="668" cy="1942" r="6"/>
    </g>
    <g fill="#4d7a17" stroke="#8dc63f" stroke-width="3">
      <circle cx="432" cy="1660" r="30"/><circle cx="392" cy="1808" r="30"/><circle cx="432" cy="1970" r="30"/>
      <circle cx="768" cy="1660" r="30"/><circle cx="808" cy="1808" r="30"/><circle cx="768" cy="1970" r="30"/>
    </g>
    <g fill="none" stroke="#fff" stroke-width="3" stroke-linecap="round">
      <path d="M420 1670 L432 1646 L444 1670 Z"/>
      <path d="M380 1816 h20 l6 -14 M388 1820 a4 4 0 1 0 0.1 0"/>
      <path d="M420 1978 h24 v-14 h-24 z"/>
      <path d="M754 1672 l28 -24"/>
      <path d="M796 1816 l24 -16 M800 1802 l16 14"/>
      <path d="M756 1978 c0 -16 24 -16 24 0 z"/>
    </g>
  </svg>
  <div class="abs core"><span class="brand-name">DORNEL<br>CONTRACTORS</span></div>

  <div class="abs service left" style="left:80px;top:1624px"><h3>Landscaping</h3>Lorem ipsum dolor sit amet, consectetur adipiscing elit, sed do eiusmod tempor</div>
  <div class="abs service left" style="left:40px;top:1774px"><h3>Mowing</h3>Lorem ipsum dolor sit amet, consectetur adipiscing elit, sed do eiusmod tempor</div>
  <div class="abs service left" style="left:80px;top:1934px"><h3>Concrete</h3>Lorem ipsum dolor sit amet, consectetur adipiscing elit, sed do eiusmod tempor</div>
  <div class="abs service" style="left:820px;top:1624px"><h3>Sidewalks</h3>Lorem ipsum dolor sit amet, consectetur adipiscing elit, sed do eiusmod tempor</div>
  <div class="abs service" style="left:860px;top:1774px"><h3>Brush Removal</h3>Lorem ipsum dolor sit amet, consectetur adipiscing elit, sed do eiusmod tempor</div>
  <div class="abs service" style="left:820px;top:1934px"><h3>Land Beautification</h3>Lorem ipsum dolor sit amet, consectetur adipiscing elit, sed do eiusmod tempor</div>

  <svg class="abs divider" style="top:2090px" viewBox="0 0 1200 60" preserveAspectRatio="none">
    <polygon points="0,50 600,10 1200,50" fill="#0a1503"/>
    <polyline points="0,50 600,10 1200,50" fill="none" stroke="#8dc63f" stroke-width="3"/>
  </svg>

  <!-- gallery -->
  <h2 class="abs title" style="top:2230px">OUR <em>GALLERY</em></h2>
  <div class="photo" style="left:144px;top:2348px;width:296px;height:282px;background:linear-gradient(160deg,#5f8a2e,#3f6a1c 60%,#2b4712)" role="img" aria-label="Lawn mower cutting grass"></div>
  <div class="photo" style="left:452px;top:2348px;width:296px;height:282px;background:linear-gradient(180deg,#2f5c23,#5b9a34 55%,#8ec34f)" role="img" aria-label="Garden with palms and stepping stones"></div>
  <div class="photo" style="left:760px;top:2348px;width:296px;height:282px;background:linear-gradient(160deg,#7a7570,#a8a29a 50%,#5e5a55)" role="img" aria-label="Fresh concrete being poured"></div>
  <div class="photo" style="left:144px;top:2640px;width:296px;height:288px;background:linear-gradient(180deg,#6b5646,#8c8c86 60%,#4c4c48)" role="img" aria-label="Paved sidewalk beside a brick wall"></div>
  <div class="photo" style="left:452px;top:2640px;width:296px;height:288px;background:linear-gradient(180deg,#6fae36,#4e8f22 60%,#3a7016)" role="img" aria-label="Freshly mowed lawn"></div>
  <div class="photo" style="left:760px;top:2640px;width:296px;height:288px;background:radial-gradient(circle at 40% 45%,#4f8a22,#2c5410 55%,#141f08)" role="img" aria-label="Trimmed round shrubs"></div>

  <!-- contact -->
  <div class="abs contact-band"></div>
  <svg class="abs divider" style="top:2970px" viewBox="0 0 1200 60" preserveAspectRatio="none">
    <polygon points="0,0 1200,0 1200,10 600,50 0,10" fill="#000"/>
    <polyline points="0,10 600,50 1200,10" fill="none" stroke="#fff" stroke-width="3"/>
  </svg>
  <h2 class="abs title" style="top:3152px">CONTACT <em>US</em></h2>

  <div class="abs col-h" style="left:144px;top:3240px">Get In Touch</div>
  <div class="field" style="left:144px;top:3294px;width:266px">Name</div>
  <div class="field" style="left:420px;top:3294px;width:266px">Phone</div>
  <div class="field" style="left:144px;top:3338px;width:542px">Email</div>
  <div class="field" style="left:144px;top:3382px;width:542px;height:60px">Message</div>
  <div class="abs btn" style="left:604px;top:3458px;font-size:13px;padding:6px 16px;border-radius:3px">Submit</div>

  <div class="abs col-h" style="left:760px;top:3240px">Contact Information</div>
  <div class="abs info" style="left:760px;top:3294px;width:320px"><span class="pin"><svg width="12" height="14" viewBox="0 0 12 14"><path d="M6 0a5 5 0 0 1 5 5c0 4-5 9-5 9S1 9 1 5a5 5 0 0 1 5-5z" fill="#2c4a0c"/></svg></span>123 Lorem ipsum dolor sit amet conse adipiscing elit</div>
  <div class="abs info" style="left:760px;top:3356px"><span class="pin"><svg width="14" height="14" viewBox="0 0 24 24"><path d="M6 3l4 5-2 2a11 11 0 0 0 6 6l2-2 5 4-2 3C10 21 3 14 3 5z" fill="#2c4a0c"/></svg></span>Phone: 1 888 888 8888</div>
  <div class="abs info" style="left:760px;top:3400px"><span class="pin"><svg width="14" height="12" viewBox="0 0 14 12"><rect x="0.5" y="0.5" width="13" height="11" fill="none" stroke="#2c4a0c"/><path d="M1 1l6 5 6-5" fill="none" stroke="#2c4a0c"/></svg></span>info@dornelcontractors.com</div>
  <div class="abs social" style="left:760px;top:3456px"><span></span><span></span><span></span><span></span><span></span><span></span></div>

  <div class="abs footer">Copyright © 2024 Dornel Contractors. All Rights Reserved. | Privacy policy</div>
</div>
</body>
</html>
```